Quorvex - Automated robotic Inspection with AI need new business cards

We need a new design of our business cards. The company is focused on automated quality control at high speed with unmatched results. We have a logo but need a more forward leaning business card that shows that we are delivering cutting edge technology.

Contact Information for Business Card

Name
Position
Adress
Phone
Email
e.g.
Lena Holmqvist
Chief Financial Officer (CFO)

Quorvex Sweden AB
Bruksvägen 14, SE-175 43 JÄRFÄLLA, Sweden
Mobile: +46735 21 47 83 | Office: +46 8 61 94 27
www.quorvex-example.com

Font styles to use
Sans Serif

```html
<!DOCTYPE html>
<html lang="en">
<head>
<meta charset="utf-8">
<title>Quorvex Business Cards</title>
<link href="https://fonts.googleapis.com/css2?family=Arimo:wght@400;700&display=swap" rel="stylesheet">
<style>
  :root {
    --page-bg: #e9e9e8;
    --card-bg: #ffffff;
    --brand-blue: #1d5289;
    --text-grey: #5b6f8c;
    --rule-grey: #8a93a8;
  }
  html, body {
    margin: 0;
    width: 1200px;
    height: 801px;
    overflow: hidden;
    background: var(--page-bg);
    font-family: "Arimo", Arial, sans-serif;
  }
  .canvas {
    position: relative;
    width: 1200px;
    height: 801px;
  }
  .card {
    position: absolute;
    top: 240px;
    width: 520px;
    height: 320px;
    background: var(--card-bg);
    border-bottom: 3px solid var(--brand-blue);
    box-shadow: 0 6px 18px rgba(0,0,0,0.12);
    box-sizing: border-box;
  }
  .card--contact { left: 60px; }
  .card--brand { left: 620px; }

  .wordmark {
    color: var(--brand-blue);
    font-weight: 700;
    display: flex;
    align-items: center;
  }
  .wordmark__dot {
    border-radius: 50%;
    background: var(--brand-blue);
    flex: none;
  }
  .card--contact .wordmark {
    position: absolute;
    left: 34px;
    top: 140px;
    font-size: 34px;
    gap: 10px;
  }
  .card--contact .wordmark__dot { width: 22px; height: 22px; }

  .card--brand .wordmark {
    position: absolute;
    left: 0; right: 0; top: 0; bottom: 0;
    justify-content: center;
    font-size: 58px;
    gap: 16px;
  }
  .card--brand .wordmark__dot { width: 36px; height: 36px; }

  .divider {
    position: absolute;
    left: 240px;
    top: 92px;
    width: 1px;
    height: 160px;
    background: var(--rule-grey);
  }
  .contact {
    position: absolute;
    left: 262px;
    top: 86px;
    color: var(--text-grey);
    font-size: 12.5px;
    line-height: 1.5;
  }
  .contact__name {
    color: var(--brand-blue);
    font-weight: 700;
    font-size: 17px;
    margin: 0;
  }
  .contact__title {
    margin: 0 0 10px;
    font-size: 13.5px;
  }
  .contact__line {
    display: flex;
    align-items: center;
    gap: 8px;
    margin: 0;
  }
  .contact__line svg {
    width: 11px;
    height: 11px;
    flex: none;
    fill: var(--brand-blue);
  }
  .contact__address {
    margin: 10px 0 0;
  }
</style>
</head>
<body>
<main class="canvas">
  <section class="card card--contact">
    <div class="wordmark"><span class="wordmark__dot"></span>Quorvex</div>
    <div class="divider"></div>
    <div class="contact">
      <p class="contact__name">Lena Holmqvist</p>
      <p class="contact__title">Chief Financial Officer (CFO)</p>
      <p class="contact__line">
        <svg viewBox="0 0 12 12" aria-hidden="true"><path d="M2.5 1 L4.5 1 L5 3.5 L3.8 4.4 C4.5 6 6 7.5 7.6 8.2 L8.5 7 L11 7.5 L11 9.5 C11 10.3 10.3 11 9.5 11 C5 11 1 7 1 2.5 C1 1.7 1.7 1 2.5 1 Z"/></svg>
        +46 8 61 94 27
      </p>
      <p class="contact__line">
        <svg viewBox="0 0 12 12" aria-hidden="true"><path d="M3 0.5 H9 A1 1 0 0 1 10 1.5 V10.5 A1 1 0 0 1 9 11.5 H3 A1 1 0 0 1 2 10.5 V1.5 A1 1 0 0 1 3 0.5 Z M3.2 1.8 V9.2 H8.8 V1.8 Z"/></svg>
        +46735 21 47 83
      </p>
      <p class="contact__line">
        <svg viewBox="0 0 12 12" aria-hidden="true"><circle cx="6" cy="6" r="5.5"/></svg>
        www.quorvex-example.com
      </p>
      <p class="contact__address">Quorvex Sweden AB, Bruksvägen 14<br>SE-175 43 JÄRFÄLLA, Sweden</p>
    </div>
  </section>

  <section class="card card--brand">
    <div class="wordmark"><span class="wordmark__dot"></span>Quorvex</div>
  </section>
</main>
</body>
</html>
```